Poly Bag Packaging Motorcycle Cables - Vorenza Brand

Poly Bag Dimensions: 33cm(H) x 24cm(W)
We would like to design a genuine Poly Bag Packaging for motorcycle cables.
Vorenza, is one of the leading companies for manufacturing Motorcycles, located in Egypt. Our company is offering high-quality products, the best in the local market, with very competitive prices.
We have a limited time to get this project done, So we Highly appreciate receiving your designs ASAP.
Target Market(s)
Motorcycle Spare parts Buyers
Colors
Designer to choose colors to be used in the design.
Look and feel

```html
<!DOCTYPE html>
<html lang="en">
<head>
<meta charset="UTF-8">
<title>Vorenza Cables Poly Bag</title>
<link rel="stylesheet" href="https://fonts.googleapis.com/css2?family=Audiowide&display=swap">
<style>
  :root {
    --page: #ffffff;
    --red: #e31b23;
    --black: #121212;
    --blue: #0a6db4;
    --yellow: #f5e21a;
    --silver: #c9cbcd;
    --clear-top: #f2f2f2;
    --cable-dark: #3a3a3a;
    --cable-mid: #6b6b6b;
  }
  * { margin: 0; padding: 0; box-sizing: border-box; }
  html, body {
    width: 1137px;
    height: 1200px;
    overflow: hidden;
    background: var(--page);
  }
  .canvas {
    position: relative;
    width: 1137px;
    height: 1200px;
  }
  .poly-bag {
    position: absolute;
    left: 200px;
    top: 54px;
    width: 798px;
    height: 1106px;
    border-radius: 22px;
    overflow: hidden;
    background: var(--clear-top);
  }
  .header-band {
    position: absolute;
    left: 0; top: 0;
    width: 100%;
    height: 100px;
    background: var(--red);
  }
  .hang-hole {
    position: absolute;
    left: 352px;
    top: 36px;
  }
  .brand-panel {
    position: absolute;
    left: 0; top: 100px;
    width: 100%;
    height: 483px;
    background: var(--black);
    display: flex;
    flex-direction: column;
    align-items: center;
    justify-content: center;
    gap: 34px;
  }
  .brand-dot {
    width: 120px;
    height: 120px;
    border-radius: 50%;
    background: var(--silver);
  }
  .brand-name {
    font-family: "Audiowide", sans-serif;
    font-size: 72px;
    letter-spacing: 4px;
    color: var(--silver);
  }
  .product-band {
    position: absolute;
    left: 0; top: 583px;
    width: 100%;
    height: 184px;
    background: var(--blue);
    display: flex;
    align-items: center;
    justify-content: center;
  }
  .product-name {
    font-family: "Audiowide", sans-serif;
    font-size: 118px;
    letter-spacing: 6px;
    color: var(--yellow);
    line-height: 1;
  }
  .window {
    position: absolute;
    left: 0; top: 767px;
    width: 100%;
    height: 229px;
    background:
      radial-gradient(ellipse 55% 60% at 58% 45%, var(--cable-dark) 0%, var(--cable-mid) 45%, rgba(230,230,230,0) 75%),
      linear-gradient(180deg, #f4f4f4, #e6e6e6);
  }
  .footer-band {
    position: absolute;
    left: 0; bottom: 0;
    width: 100%;
    height: 110px;
    background: var(--red);
    display: flex;
    align-items: center;
    justify-content: center;
  }
  .tagline {
    font-family: "Audiowide", sans-serif;
    font-size: 44px;
    letter-spacing: 3px;
    color: var(--yellow);
  }
</style>
</head>
<body>
<div class="canvas">
  <div class="poly-bag">
    <div class="header-band"></div>
    <svg class="hang-hole" width="96" height="50" viewBox="0 0 96 50" aria-hidden="true">
      <path d="M10 14 H38 A10 10 0 0 1 58 14 H86 A10 10 0 0 1 96 24 V40 A10 10 0 0 1 86 50 H10 A10 10 0 0 1 0 40 V24 A10 10 0 0 1 10 14 Z" fill="#ffffff"/>
    </svg>
    <div class="brand-panel">
      <div class="brand-dot"></div>
      <div class="brand-name">VORENZA</div>
    </div>
    <div class="product-band">
      <div class="product-name">CABLES</div>
    </div>
    <div class="window" role="img" aria-label="Coiled black motorcycle wiring harness with ring terminal visible through clear bag"></div>
    <div class="footer-band">
      <div class="tagline">HIGH-QUALITY</div>
    </div>
  </div>
</div>
</body>
</html>
```